Real Estate Investor needs awesome business card design

I invest in real estate, focused on multi-family properties, and I need a business card to hand out to potential partners. I prefer simple, clean designs, but it needs to stand out, so I'd like there to be a bit of red in the design as well.

It should include this information:

Front
Calder Whitby
Real Estate Investor
Direct phone: 501-555-0187
Email: calderjwhitby@mailbox-example.net
Headshot (Picture), I've uploaded a few, just pick the one you think looks best with your design. You can remove the background from the headshot image if it looks better.

Back
The back of the card's design should flow and be congruent with the front. On the back I want to put an inspirational quote or question. There will be different ones depending on the card, so I'll need the original file so I can edit it in the end.

For now, use “The Pessimist Sees Difficulty In Every Opportunity. The Optimist Sees The Opportunity In Every Difficulty.” -Edmund Halvorsen

Target Market(s)

Investors

Industry/Entity Type

Real Estate

Contact Information for Business Card

Front
Calder Whitby
Real Estate Investor

Back
The back of the card's design should flow and be congruent with the front. On the back I want to put an inspirational quote or question. There will be different ones depending on the card, so I'll need the original file so I can edit it in the end. I've uploaded some EXAMPLES of business cards with quotes on them. Don't copy but feel free to use them as inspiration.

The design will be printed on "ZAP sized" business cards
1039 x 697 pixels
with rounded corners

Font styles to use
Serif
Decorative
Script

Colors
ec1f27

Requirements
Must have
• Headshot, name, and other information in it.
• 1039 x 697 pixels
• Rounded corners
• Clean design that pops. I'm open to see any color background, including black.
• Headshots can be located here: https://www.filecrate-example.com/sh/8kx2vq71ld0pa3z/BQQTXL7mrrf9eT3Kq0HhgkLm2b?dl=0
Nice to have
• It would be awesome if the design included a personal signature or monogram, but if not I'll get a personal logo developed later and the card redesigned if I think it needs it.
Should not have
• Cluttered design

```html
<!DOCTYPE html>
<html lang="en">
<head>
<meta charset="utf-8">
<title>Calder Whitby – Business Card</title>
<link href="https://fonts.googleapis.com/css2?family=Lato:wght@300&family=Open+Sans:wght@400&display=swap" rel="stylesheet">
<style>
  :root {
    --page: #d4d4d4;
    --card-dark: #070707;
    --card-mid: #1a1a1a;
    --ink: #ffffff;
    --accent: #ec1f27;
    --accent-soft: #f0353c;
  }
  * { margin: 0; padding: 0; box-sizing: border-box; }
  html, body {
    width: 1189px; height: 1200px; overflow: hidden;
    background: var(--page);
  }
  .sheet {
    position: relative; width: 1189px; height: 1200px;
  }
  .card {
    position: absolute; left: 174px; width: 840px; height: 478px;
    background: linear-gradient(125deg, var(--card-mid) 0%, var(--card-dark) 35%, var(--card-dark) 50%, var(--card-mid) 75%, #101010 100%);
    overflow: hidden;
    color: var(--ink);
  }
  .card--front { top: 92px; }
  .card--back { top: 630px; }

  .headshot {
    position: absolute; left: 45px; top: 81px; width: 189px; height: 257px;
    background: linear-gradient(160deg, #4a4a4a 0%, #2a2a2a 55%, #161616 100%);
  }
  .identity {
    position: absolute; right: 47px; top: 72px; text-align: right;
  }
  .name {
    font-family: "Lato", sans-serif; font-weight: 300;
    font-size: 46px; line-height: 1; letter-spacing: 3px; text-transform: uppercase;
  }
  .role {
    font-family: "Open Sans", sans-serif; font-weight: 400;
    color: var(--accent); font-size: 23px; letter-spacing: 1.2px; line-height: 1.1;
    margin-top: 1px;
  }
  .contact {
    position: absolute; right: 47px; top: 280px; list-style: none;
    font-family: "Open Sans", sans-serif; font-size: 23px;
  }
  .contact li {
    display: flex; justify-content: flex-end; align-items: center; gap: 17px;
    height: 34px;
  }
  .contact-icon {
    width: 24px; height: 24px; background: var(--accent);
    display: flex; align-items: center; justify-content: center;
  }
  .wave {
    position: absolute; inset: 0; width: 100%; height: 100%;
  }

  .card--back .identity {
    left: 0; right: 0; top: 152px; text-align: center;
  }
  .card--back .name { font-size: 62px; letter-spacing: 5px; }
  .card--back .role { font-size: 32px; letter-spacing: 1.6px; margin-top: 2px; }
  .quote {
    position: absolute; left: 0; right: 0; top: 346px; text-align: center;
    font-family: "Open Sans", sans-serif; font-size: 16.5px; line-height: 23px;
    letter-spacing: 1px;
  }
  .quote cite { display: block; font-style: normal; }
</style>
</head>
<body>
<main class="sheet">
  <section class="card card--front">
    <svg class="wave" viewBox="0 0 990 564" preserveAspectRatio="none" aria-hidden="true">
      <defs>
        <linearGradient id="redSweep" x1="0" x2="1" y1="0" y2="0">
          <stop offset="0" stop-color="#e8141d"/>
          <stop offset="1" stop-color="#f0353c"/>
        </linearGradient>
      </defs>
      <path d="M110 564 C 400 522, 690 514, 780 511 C 880 508, 935 470, 990 386 L990 564 Z" fill="#ffffff"/>
      <path d="M225 564 C 500 530, 700 522, 790 520 C 890 517, 948 482, 990 410 L990 564 Z" fill="url(#redSweep)"/>
    </svg>
    <div class="headshot" role="img" aria-label="Black and white headshot of Calder Whitby in a dark blazer"></div>
    <header class="identity">
      <h1 class="name">Calder Whitby</h1>
      <p class="role">Real Estate Investor</p>
    </header>
    <ul class="contact">
      <li>
        <span>501-555-0187</span>
        <span class="contact-icon">
          <svg width="16" height="14" viewBox="0 0 16 14" aria-hidden="true">
            <path d="M1 4 C1 1.5 15 1.5 15 4 L15 5.5 L11.5 5.5 L11.5 4 L4.5 4 L4.5 5.5 L1 5.5 Z" fill="#fff"/>
            <path d="M4 6.5 L12 6.5 L14 13 L2 13 Z" fill="#fff"/>
            <circle cx="8" cy="9.5" r="1.8" fill="#ec1f27"/>
          </svg>
        </span>
      </li>
      <li>
        <span>calderjwhitby@mailbox-example.net</span>
        <span class="contact-icon">
          <svg width="16" height="12" viewBox="0 0 16 12" aria-hidden="true">
            <rect x="1" y="1" width="14" height="10" fill="none" stroke="#fff" stroke-width="1.3"/>
            <path d="M1 1 L8 7 L15 1 M1 11 L6 6 M15 11 L10 6" fill="none" stroke="#fff" stroke-width="1.3"/>
          </svg>
        </span>
      </li>
    </ul>
  </section>

  <section class="card card--back">
    <header class="identity">
      <h2 class="name">Calder Whitby</h2>
      <p class="role">Real Estate Investor</p>
    </header>
    <blockquote class="quote">
      <p>The Pessimist Sees Difficulty In Every Opportunity. The Optimist Sees The<br>Opportunity In Every Difficulty.</p>
      <cite>-Edmund Halvorsen-</cite>
    </blockquote>
  </section>
</main>
</body>
</html>
```